Lift display layouts for global brand

We need display layouts for different sizes and applications of display. All layouts must include an arrow and floor position number. I will upload some basic examples. We want these to look modern and really eye-catching but suitable for the space it is meant for.

By "layout" we mean design specifically created for the space - including arrow, floor number, widgets / background graphics etc.
Display type ONE 15" (1024 x 768 pixels)
a. Hotel theme layout (logo, floor position, arrow and simple weather widget) [Landscape]
b. Layout displaying live TV news broadcast or similar [Landscape]
Display type TWO 10.4” (800 x 600 pixels)
a. Shopping centre layout + shop advert in main space [Landscape]
b. Office tenant standard layout + business logo in main space [Portrait]
c. Spa / Leisure Centre Layout [Landscape]
Display type 38” (1920 x 540 pixels)
a. Airport/Train station layout + flight/train departure information in main space [Landscape]
b. Restaurant layout + Menu in main space [Portrait]
c. Shopping Centre layout + Centre map in main space [Landscape]
Display type 21.5” (1920 x 1080 pixels)
a. Skyscraper layout + lift buttons and building history text [Portrait]
Display type 7” (800x480)
a. Simple lift position indicator arrow and floor [Landscape]
b. Lift position indicator with arrow and showing pictogram (Alarm, Maintenance or similar) [Landscape]

```html
<!DOCTYPE html>
<html lang="en">
<head>
<meta charset="utf-8">
<title>Lift Display – Live News Layout</title>
<link rel="stylesheet" href="https://fonts.googleapis.com/css2?family=Lato:wght@300&family=Montserrat:wght@600;700&display=swap">
<style>
  :root {
    --orange-deep: #b8330f;
    --orange-mid: #d9561a;
    --orange-warm: #e8742a;
    --tan: #d98a4a;
    --wine: #6a0c22;
    --sun: #fff1cf;
    --badge: #f7a928;
    --white: #ffffff;
    --studio-red: #9a2336;
    --studio-steel: #3d5680;
    --studio-window: #3f7fc4;
    --studio-dark: #1a2646;
    --news-blue: #1d3f95;
    --news-blue-dark: #13296a;
  }
  * { margin: 0; padding: 0; box-sizing: border-box; }
  html, body { width: 1200px; height: 900px; overflow: hidden; }
  body { position: relative; background: var(--orange-deep); font-family: "Montserrat", sans-serif; }

  .hotel-backdrop {
    position: absolute; inset: 0;
    background:
      /* sunlit balcony window */
      radial-gradient(ellipse 200px 260px at 1010px 210px, rgba(255,246,220,1), rgba(255,214,150,0.75) 45%, rgba(255,170,90,0) 100%),
      linear-gradient(90deg, rgba(0,0,0,0) 0 803px, rgba(255,170,90,0.35) 803px 830px, rgba(255,200,130,0.55) 830px 1170px, rgba(150,70,20,0.4) 1170px),
      /* floor on the right */
      linear-gradient(180deg, rgba(0,0,0,0) 0 440px, rgba(190,80,30,0.35) 440px),
      /* bed and pillows band on the left */
      radial-gradient(ellipse 520px 70px at 380px 300px, rgba(230,120,60,0.55), rgba(230,120,60,0) 100%),
      radial-gradient(ellipse 300px 160px at 120px 430px, rgba(240,140,80,0.45), rgba(240,140,80,0) 100%),
      /* ceiling shade */
      linear-gradient(180deg, rgba(150,50,10,0.35) 0%, rgba(0,0,0,0) 12%),
      linear-gradient(180deg, var(--orange-warm) 0%, var(--orange-mid) 30%, #c2451a 50%, #9a2a22 72%, var(--wine) 100%);
  }

  .direction-badge {
    position: absolute; left: 158px; top: 79px;
    width: 188px; height: 188px;
  }

  .floor-number {
    position: absolute; left: 505px; top: 60px;
    font-family: "Lato", sans-serif; font-weight: 300;
    font-size: 208px; line-height: 1; letter-spacing: -4px;
    color: var(--white);
  }

  .news-panel {
    position: absolute; left: 150px; top: 311px;
    width: 922px; height: 521px;
    border: 6px solid var(--white);
    box-shadow: 0 6px 18px rgba(0,0,0,0.3);
    overflow: hidden;
  }
  .news-broadcast {
    position: absolute; inset: 0;
    background:
      /* red studio ceiling */
      linear-gradient(180deg, var(--studio-red) 0%, rgba(154,35,54,0.6) 6%, rgba(154,35,54,0) 13%),
      /* bright skyline windows on the right */
      radial-gradient(ellipse 260px 150px at 700px 150px, rgba(120,170,225,0.9), rgba(63,127,196,0) 100%),
      /* monitor wall glow on the left */
      radial-gradient(ellipse 180px 140px at 260px 140px, rgba(90,130,180,0.7), rgba(60,90,140,0) 100%),
      /* presenters zone, darker suits */
      radial-gradient(ellipse 200px 200px at 130px 260px, rgba(20,25,45,0.7), rgba(20,25,45,0) 100%),
      radial-gradient(ellipse 160px 220px at 820px 260px, rgba(20,30,60,0.7), rgba(20,30,60,0) 100%),
      linear-gradient(180deg, #4a4f70 0%, var(--studio-steel) 22%, var(--studio-window) 45%, #2b4e8a 65%, var(--studio-dark) 100%);
  }
  .news-caption {
    position: absolute; left: 0; right: 0; bottom: 0; height: 250px;
    background: linear-gradient(180deg, rgba(29,63,149,0) 0%, rgba(29,63,149,0.85) 38%, var(--news-blue) 70%, var(--news-blue-dark) 100%);
    display: flex; flex-direction: column; align-items: center; justify-content: flex-end;
    padding-bottom: 68px;
    color: var(--white); text-align: center;
  }
  .news-caption .headline {
    font-weight: 700; font-size: 76px; line-height: 1; letter-spacing: 1.5px;
    text-shadow: 0 2px 6px rgba(0,0,0,0.35);
  }
  .news-caption .cta {
    font-weight: 600; font-size: 50px; line-height: 1; letter-spacing: 0.5px;
  }
</style>
</head>
<body>
  <div class="hotel-backdrop" role="img" aria-label="Hotel room with bed and pillows and a couple looking out of a sunlit balcony window, warm orange tint"></div>

  <svg class="direction-badge" viewBox="0 0 188 188" aria-label="Going up">
    <circle cx="94" cy="94" r="94" fill="var(--badge)"/>
    <circle cx="94" cy="94" r="60" fill="none" stroke="var(--white)" stroke-width="9"/>
    <path d="M94 136 V58 M64 88 L94 58 L124 88" fill="none" stroke="var(--white)" stroke-width="9" stroke-linecap="round" stroke-linejoin="round"/>
  </svg>

  <div class="floor-number">18</div>

  <section class="news-panel">
    <div class="news-broadcast" role="img" aria-label="Live TV news studio with three presenters at the anchor desk and a city skyline behind the windows"></div>
    <div class="news-caption">
      <div class="headline">LIVE NEWS</div>
      <div class="cta">CLICK HERE</div>
    </div>
  </section>
</body>
</html>
```